BRCW Business Cards

Business Cards should contain:
Bright Ridgecrest Coating Works
Felix Darrow
M: 0417 865 093
E: brightRCW@fernpost.example
BRCW logo
TCG logo
Painting & Decorating
Licence # 719362K
slogan: feel the mark of modern perfection

Target Market(s)

all aspect of painting

Industry/Entity Type

Trade

Contact Information for Business Card

Felix Darrow
M: 0417 865 093
E: brightRCW@fernpost.example
BRCW logo
TCG logo
Painting & Decorating
Licence # 719362K

Font styles to use
Serif
Sans Serif

Requirements
Must have
• clear design with nice backround
• two sides
• smal TCG logo
Nice to have
• easy to read
Should not have
• mess
• black
• plastics form

```html
<!DOCTYPE html>
<html lang="en">
<head>
<meta charset="utf-8">
<title>BRCW Business Cards</title>
<link rel="stylesheet" href="https://fonts.googleapis.com/css2?family=Lora:ital,wght@0,500;0,700;1,500&family=Open+Sans:wght@400;600;700&display=swap">
<style>
  :root {
    --teal: #1f5a52;
    --teal-dark: #17463f;
    --leaf: #3a8a2e;
    --ink: #3f3f3f;
    --paper: #ffffff;
    --stage: #e9ece9;
    --badge: #5b86c4;
    --sky: #9cc4e4;
    --facade: #c9b48f;
  }
  * { box-sizing: border-box; margin: 0; padding: 0; }
  html, body { width: 1200px; height: 900px; overflow: hidden; }
  body {
    background: var(--stage);
    font-family: "Open Sans", Arial, sans-serif;
    position: relative;
  }
  .card {
    position: absolute;
    left: 250px;
    width: 700px;
    height: 400px;
    background: var(--paper);
    box-shadow: 0 4px 14px rgba(0,0,0,0.12);
    overflow: hidden;
  }
  /* Back side */
  .card--back { top: 40px; }
  .slogan {
    position: absolute;
    left: 40px;
    right: 40px;
    top: 156px;
    font-family: "Lora", Georgia, serif;
    font-weight: 700;
    font-size: 33px;
    color: var(--teal);
    white-space: nowrap;
  }
  .slogan__feature {
    position: relative;
    display: inline-block;
    padding: 2px 8px;
    margin: 0 3px;
    vertical-align: middle;
  }
  .slogan__photo {
    position: absolute;
    inset: -12px 0 -6px 0;
    border-radius: 6px;
    background: linear-gradient(160deg, var(--sky) 0%, #d8e6ef 45%, var(--facade) 100%);
  }
  .slogan__word {
    position: relative;
    color: #f4f7f8;
    font-style: italic;
    font-weight: 500;
  }
  .tagline {
    position: absolute;
    right: 90px;
    top: 212px;
    font-family: "Lora", Georgia, serif;
    font-style: italic;
    font-weight: 500;
    font-size: 20px;
    color: var(--teal);
  }
  .back-marks {
    position: absolute;
    right: 50px;
    bottom: 48px;
    display: flex;
    align-items: center;
    gap: 34px;
  }
  .partner-badge {
    width: 58px;
    height: 58px;
    border-radius: 50%;
    background: var(--badge);
    opacity: 0.85;
  }
  .brand-small {
    display: flex;
    align-items: center;
    gap: 10px;
    font-family: "Lora", Georgia, serif;
    font-weight: 500;
    font-size: 30px;
    color: var(--teal);
  }
  .brand-small__square { width: 26px; height: 26px; background: var(--leaf); }

  /* Front side */
  .card--front {
    top: 470px;
    border: 14px solid var(--teal);
  }
  .brand {
    position: absolute;
    left: 190px;
    top: 36px;
    display: flex;
    align-items: flex-start;
    gap: 22px;
  }
  .brand__square {
    width: 70px;
    height: 70px;
    margin-top: 12px;
    background: var(--leaf);
  }
  .brand__text {
    font-family: "Lora", Georgia, serif;
    font-weight: 500;
    color: var(--teal);
    line-height: 1.1;
  }
  .brand__initials { font-size: 60px; letter-spacing: 2px; }
  .brand__name { font-size: 24px; }
  .contact {
    position: absolute;
    left: 70px;
    top: 200px;
    color: var(--ink);
  }
  .contact__name {
    font-weight: 700;
    font-size: 21px;
    color: var(--teal);
    margin-bottom: 12px;
  }
  .contact__line {
    display: flex;
    align-items: center;
    gap: 10px;
    font-size: 18px;
    margin-bottom: 6px;
  }
  .contact__icon { width: 16px; height: 18px; flex: none; }
  .contact__at { font-size: 18px; width: 16px; text-align: center; }
  .licence {
    position: absolute;
    right: 44px;
    bottom: 60px;
    font-weight: 700;
    font-size: 19px;
    color: var(--leaf);
  }
</style>
</head>
<body>
  <section class="card card--back" aria-label="Card back">
    <p class="slogan">Feel the <span class="slogan__feature"><span class="slogan__photo" role="img" aria-label="Photo of a freshly painted modern building"></span><span class="slogan__word">mark</span></span> of modern perfection</p>
    <p class="tagline">~Painting &amp; Decorating~</p>
    <div class="back-marks">
      <div class="partner-badge" role="img" aria-label="TCG association badge"></div>
      <div class="brand-small"><span class="brand-small__square"></span>BRCW</div>
    </div>
  </section>

  <section class="card card--front" aria-label="Card front">
    <div class="brand">
      <span class="brand__square"></span>
      <div class="brand__text">
        <div class="brand__initials">BRCW</div>
        <div class="brand__name">Bright Ridgecrest<br>Coating Works</div>
      </div>
    </div>
    <div class="contact">
      <p class="contact__name">Felix Darrow</p>
      <p class="contact__line">
        <svg class="contact__icon" viewBox="0 0 16 18" aria-hidden="true">
          <rect x="3.5" y="1" width="9" height="16" rx="1.8" fill="none" stroke="#3f3f3f" stroke-width="1.6"/>
          <circle cx="8" cy="14" r="1" fill="#3f3f3f"/>
        </svg>
        0417 865 093
      </p>
      <p class="contact__line"><span class="contact__at">@</span>brightRCW@fernpost.example</p>
    </div>
    <p class="licence">Licence # 719362K</p>
  </section>
</body>
</html>
```